Velora Services group

Velora services group is a facility services company provide security and cleaning services to corporate and retail sectors, we need high quality business card design for our company, the main company is (velora services group) and the other companies is (velora security group) and (velora cleaning group), I have attached 3 logos the main logo is velora services group and the other logos will be smaller.
Business card details:
Marco Delvecki
General Manager
Velora Services Group
Mobil: 0427 615 392
Tell: 1300 457 206
Email: marco@veloraservices-example.com.au
Web: www.veloraservices-example.com.au
12/5-9 Tambor Street Corwen Vale NSW 2611
Services: Security, Cleaning, Facility Services
Slogan: Services, Protection, Integrity

```html
<!DOCTYPE html>
<html lang="en">
<head>
<meta charset="utf-8">
<title>Velora Services Group – Business Card</title>
<link href="https://fonts.googleapis.com/css2?family=Andika:wght@400;700&family=Open+Sans:wght@600&display=swap" rel="stylesheet">
<style>
  :root {
    --navy: #1f3a5a;
    --red: #d9202a;
    --white: #ffffff;
    --ink: #1c2c4a;
    --phone-blue: #1d6fc1;
    --backdrop: #e9eaec;
  }
  * { box-sizing: border-box; margin: 0; padding: 0; }
  html, body { width: 1200px; height: 977px; overflow: hidden; }
  body {
    background: var(--backdrop);
    font-family: "Andika", sans-serif;
    color: var(--ink);
    display: flex;
    flex-direction: column;
    align-items: center;
    justify-content: center;
    gap: 36px;
  }
  .card {
    width: 720px;
    height: 440px;
    padding: 24px;
    box-shadow: 0 4px 14px rgba(0,0,0,.15);
  }
  .card--front { background: var(--red); }
  .card--back { background: var(--navy); }
  .card__face {
    width: 100%;
    height: 100%;
    background: var(--white);
    position: relative;
  }

  /* Brand name lockups */
  .brand { font-weight: 700; color: var(--navy); display: flex; align-items: center; gap: 10px; line-height: 1.05; white-space: nowrap; }
  .brand__mark { background: var(--navy); flex: none; }
  .brand--main { font-size: 34px; }
  .brand--main .brand__mark { width: 26px; height: 26px; }
  .brand--back { font-size: 22px; }
  .brand--back .brand__mark { width: 20px; height: 20px; }
  .brand--sub { font-size: 18px; gap: 8px; }
  .brand--sub .brand__mark { width: 13px; height: 13px; }

  .slogan { color: var(--red); font-size: 17px; letter-spacing: .5px; margin-top: 8px; white-space: nowrap; }
  .slogan--back { font-size: 15px; }

  /* Front */
  .front__main { position: absolute; top: 40px; left: 0; right: 0; display: flex; flex-direction: column; align-items: center; }
  .front__cleaning { position: absolute; left: 40px; top: 160px; }
  .front__security { position: absolute; right: 40px; top: 245px; }
  .services-band {
    position: absolute; left: 40px; right: 40px; bottom: 36px;
    background: var(--navy); color: var(--white);
    font-family: "Open Sans", sans-serif; font-weight: 600; font-size: 21px;
    text-align: center; padding: 7px 12px; letter-spacing: .3px;
  }

  /* Back */
  .back__logo { position: absolute; left: 22px; top: 140px; }
  .back__divider { position: absolute; left: 300px; top: 30px; bottom: 30px; width: 2px; background: var(--ink); }
  .contact { position: absolute; left: 322px; top: 26px; right: 10px; }
  .contact__name { font-size: 30px; font-weight: 700; color: var(--navy); line-height: 1.1; }
  .contact__name span { color: var(--red); }
  .contact__role { font-size: 19px; margin: 2px 0 14px 30px; }
  .contact__list { list-style: none; }
  .contact__item { display: flex; align-items: flex-start; gap: 12px; font-size: 16px; line-height: 1.25; margin-bottom: 12px; white-space: nowrap; }
  .contact__icon { width: 20px; height: 20px; flex: none; fill: var(--navy); }
  .contact__icon--phone { fill: var(--phone-blue); }
</style>
</head>
<body>

  <section class="card card--front" aria-label="Card front">
    <div class="card__face">
      <div class="front__main">
        <div class="brand brand--main"><span class="brand__mark"></span>Velora Services Group</div>
        <p class="slogan">Services | Protection | Integrity</p>
      </div>
      <div class="front__cleaning">
        <div class="brand brand--sub"><span class="brand__mark"></span>Velora Cleaning Group</div>
      </div>
      <div class="front__security">
        <div class="brand brand--sub"><span class="brand__mark"></span>Velora Security Group</div>
      </div>
      <p class="services-band">Services: Security | Cleaning | Facility Services</p>
    </div>
  </section>

  <section class="card card--back" aria-label="Card back">
    <div class="card__face">
      <div class="back__logo">
        <div class="brand brand--back"><span class="brand__mark"></span>Velora Services Group</div>
        <p class="slogan slogan--back">Services | Protection | Integrity</p>
      </div>
      <div class="back__divider"></div>
      <div class="contact">
        <h1 class="contact__name">Marco <span>Delvecki</span></h1>
        <p class="contact__role">General Manager</p>
        <ul class="contact__list">
          <li class="contact__item">
            <svg class="contact__icon" viewBox="0 0 20 20"><rect x="5" y="1" width="10" height="18" rx="2" fill="none" stroke="#1f3a5a" stroke-width="2"/><rect x="7" y="4" width="6" height="8" fill="#1f3a5a"/></svg>
            0427 615 392
          </li>
          <li class="contact__item">
            <svg class="contact__icon contact__icon--phone" viewBox="0 0 20 20"><path d="M5 2l3 4-2 2c1 3 3 5 6 6l2-2 4 3-2 3C9 18 2 11 2 4z"/></svg>
            1300 457 206
          </li>
          <li class="contact__item">
            <svg class="contact__icon" viewBox="0 0 20 20"><rect x="1" y="4" width="18" height="12"/><path d="M1 4l9 7 9-7" fill="none" stroke="#fff" stroke-width="1.5"/></svg>
            marco@veloraservices-example.com.au
          </li>
          <li class="contact__item">
            <svg class="contact__icon" viewBox="0 0 20 20"><circle cx="10" cy="10" r="8.5"/><path d="M1.5 10h17M10 1.5c-4 4-4 13 0 17M10 1.5c4 4 4 13 0 17" fill="none" stroke="#fff" stroke-width="1.2"/></svg>
            veloraservices-example.com.au
          </li>
          <li class="contact__item">
            <svg class="contact__icon" viewBox="0 0 20 20"><path d="M10 1a6 6 0 0 0-6 6c0 5 6 12 6 12s6-7 6-12a6 6 0 0 0-6-6z"/><circle cx="10" cy="7" r="2.3" fill="#fff"/></svg>
            <span>12/5-9 Tambor Street<br>Corwen Vale NSW 2611</span>
          </li>
        </ul>
      </div>
    </div>
  </section>

</body>
</html>
```